Wordpress Design Project

Hello, my name is Mervin Tolle and I am a Professor at a university in Hong Kong. I am looking for a clean and professional website to introduce myself with my bio, resume, and contact info. Looking for a creative & professional personal website, because all the information is very textual and I am looking forward to see how you can make it look good.
Updates
Project Deadline Extended
Reason: Can't find a satisfying design so far. Looking forward to see better ones.
I have added a zip file call "Good Examples" please look at the screenshot I attach. These are the quality that I am looking forward to see in your work.
Project Deadline Extended
Reason: It looks like we need more time
Project Deadline Extended
Reason: Need more time, waiting for designs
Target Market(s)
Potential Business Clients & Partners
Industry/Entity Type
University
Requirements
Must have
- The Design:
Please include photos of the schools I went to, e.g. Brelford University in Michigan, read my resume for more. You can also download the logos of the organization or institute and include them in my website to make the website more professional, just make sure the logo you found on google is correct.
The Development:
The final deliverable must be a fully coded, functional website. Site must be tested and good to go in IE 7+, Firefox 9+, Chrome and both Apple and Android Mobile platforms. Blog must be one that church can easily upload content to as an integrated part of the site (no Postwick.com, etc plugins please).
Final handover must include full rights to the designs, stock art, coding, etc (so, no "one use templates" please).
Final handover will include loading and testing on to our hosting server.
The designer must be willing to support the site for 30 days after launch as part of the site payment.
Nice to have
- I have attached some scanned photos of myself. They are really blurry and low quality, can you do some touch ups in photoshop? Because I would still love to have the photos appear somewhere in the website (e.g. inside a banner).
You can also find my photos on google by searching my name "Mervin Tolle", just make sure you find the right one.
Should not have
- Anything that looks cheap and amateurish, no flash. Anything that looks like a cookie cutter website.

```html
<!DOCTYPE html>
<html lang="en">
<head>
<meta charset="utf-8">
<title>Mervin Tolle – Professor of Management</title>
<link rel="stylesheet" href="https://fonts.googleapis.com/css2?family=Source+Sans+3:wght@400;600;700&family=Arimo:ital,wght@0,400;0,700;1,700&display=swap">
<style>
:root{
  --blue:#0e5ca7;
  --heading:#0d4a86;
  --text:#333;
  --panel:#efefef;
  --footer:#3e3e3e;
  --footer-text:#b9b9b9;
  --footer-brand:#e6e6e6;
  --dark:#1c1c1c;
}
*{box-sizing:border-box;margin:0;padding:0}
html,body{width:1165px;height:1200px;overflow:hidden}
body{position:relative;background:#fff;font-family:"Arimo",Arial,sans-serif;color:var(--text);font-size:12px}
.abs{position:absolute}
.brand{display:flex;align-items:center;gap:12px;font-family:"Source Sans 3",sans-serif;font-weight:700;color:var(--blue);font-size:24px;line-height:1}
.brand .dot{width:44px;height:44px;border-radius:50%;background:var(--blue)}
.footer-brand{color:var(--footer-brand);font-size:22px}
.footer-brand .dot{background:#bdbdbd}
.header-top{left:0;top:0;width:1165px;height:3px;background:#111}
.call{left:650px;top:50px;font-family:"Source Sans 3",sans-serif;font-size:22px;color:var(--blue)}
.call b{color:#444;font-weight:400;font-size:24px}
.follow{left:864px;top:34px;width:274px;height:56px;background:linear-gradient(#fff,#f1f1f1)}
.follow-label{left:958px;top:22px;font-size:12px;font-weight:700;color:#777}
.social{left:906px;top:44px;display:flex;gap:6px}
.social span{width:30px;height:30px;border-radius:50%;background:radial-gradient(circle at 40% 35%,#fafafa,#9a9a9a);box-shadow:0 2px 3px rgba(0,0,0,.3)}
.social svg{display:block;margin:8px auto}
.nav{left:0;top:100px;width:1165px;height:34px;background:var(--blue)}
.nav ul{position:absolute;left:109px;top:0;display:flex;list-style:none;height:34px;align-items:center}
.nav li{font-family:"Source Sans 3",sans-serif;font-size:13px;font-weight:600;color:#fff;padding:0 19px;border-left:1px solid #4d86c1}
.nav li:first-child{padding-left:0;border:0}
.search{left:864px;top:107px;width:179px;height:19px;background:#fff;border:1px solid #ccc;font-size:12px;color:#999;padding:2px 3px}
.search svg{position:absolute;right:3px;top:2px}
.stage{left:0;top:134px;width:1165px;height:380px;background:linear-gradient(#e9e9e9,#f5f5f5 80%,#fff)}
.shadow{left:120px;top:470px;width:925px;height:40px;border-radius:50%;background:radial-gradient(ellipse at 50% 20%,rgba(0,0,0,.55),rgba(0,0,0,0) 70%)}
.banner{left:108px;top:146px;width:945px;height:324px;background:#111;border:2px dashed #666;outline:3px solid #111}
.banner-photo{left:4px;top:4px;width:706px;height:316px;background:linear-gradient(110deg,#c9d8e6 0%,#8a98a8 35%,#f2b53b 65%,#f7c74a 100%)}
.caption{left:4px;top:255px;width:706px;height:65px;background:rgba(40,40,40,.82);color:#fff;font-family:"Source Sans 3",sans-serif;font-weight:700;font-size:23px;line-height:29px;padding:4px 14px}
.tabs{left:712px;top:4px;width:227px;height:316px;display:flex;background:linear-gradient(90deg,#1b1b1b,#2a2a2a)}
.tab{width:51px;border-right:1px solid #444;position:relative}
.tab span{position:absolute;left:14px;bottom:40px;transform:rotate(-90deg);transform-origin:left bottom;white-space:nowrap;translate:16px 0;color:#fff;font-weight:700;font-size:14px;letter-spacing:.3px}
.page-title{position:absolute;left:112px;top:524px;font-family:"Source Sans 3",sans-serif;font-weight:600;font-size:26px;color:var(--heading)}
.intro-photo{left:112px;top:570px;width:193px;height:137px;background:#ddd;padding:5px}
.intro-photo div{width:100%;height:100%;background:linear-gradient(135deg,#7f9fc4,#cfd6dd 50%,#8ab06a)}
.intro{left:316px;top:572px;width:470px;line-height:17.5px;font-size:12px}
.intro2{left:114px;top:717px;width:676px;line-height:17.5px;font-size:12px}
.readmore{left:694px;top:773px;width:86px;height:23px;background:var(--dark);color:#fff;border-radius:4px;font-size:12px;text-align:center;line-height:23px}
.card{width:210px}
.card .frame{width:206px;height:116px;border:1px solid #ddd;padding:6px;background:#fff}
.card .pic{width:100%;height:100%;position:relative}
.card .pic b{position:absolute;left:0;bottom:0;width:100%;height:27px;background:rgba(40,40,40,.8);color:#fff;font-family:"Source Sans 3",sans-serif;font-size:17px;letter-spacing:.5px;padding:1px 8px}
.card p{margin:8px 6px 0;line-height:18px;font-size:12px}
.card .more{display:block;text-align:right;color:var(--blue);font-weight:700;font-style:italic;font-size:12px;margin-top:3px}
.side{left:818px;width:232px;background:var(--panel);border-radius:4px}
.side h2{margin:4px 5px 0;height:31px;background:var(--blue);border-radius:4px;color:#fff;font-family:"Source Sans 3",sans-serif;font-weight:600;font-size:21px;padding:0 7px;line-height:31px}
.news{display:flex;gap:7px;margin:16px 0 0 14px;position:relative;height:48px}
.news .thumb{width:42px;height:34px;border:1px solid #ccc;background:linear-gradient(#bfc7cf,#8d98a3);flex:none}
.news p{font-weight:700;color:#444;font-size:12px;line-height:14px;width:165px}
.news p span{font-weight:400}
.news i{position:absolute;right:12px;top:44px;font-style:normal;font-size:11px;color:#444}
.quote{margin:18px 12px 0 22px;font-size:13.5px;line-height:18px;color:#444;position:relative}
.quote:before{content:"\201C";position:absolute;left:-17px;top:-9px;font-size:30px;font-family:Georgia,serif}
.quote:after{content:"\201D";position:absolute;right:-2px;bottom:-24px;font-size:30px;font-family:Georgia,serif}
.footer{left:0;top:1089px;width:1165px;height:111px;background:var(--footer)}
.foot-nav{left:348px;top:1126px;color:var(--footer-text);font-size:13px;word-spacing:2px}
.copy{left:347px;top:1150px;color:var(--footer-text);font-size:12px}
.addr{right:113px;top:1106px;text-align:right;color:var(--footer-text);font-size:12px;line-height:20px}
</style>
</head>
<body>
<div class="abs header-top"></div>
<div class="abs brand" style="left:112px;top:28px"><span>Harbourview<br>School</span><span class="dot"></span></div>
<div class="abs follow"></div>
<div class="abs follow-label">Follow Us on:</div>
<div class="abs social">
  <span></span><span></span><span></span>
  <span><svg width="16" height="12" viewBox="0 0 16 12"><rect x=".5" y=".5" width="15" height="11" fill="none" stroke="#555"/><path d="M1 1l7 6 7-6" fill="none" stroke="#555"/></svg></span>
</div>
<div class="abs call">Call us: <b>123 4567 890</b></div>

<nav class="abs nav"><ul><li>HOME</li><li>ABOUT US</li><li>BIO</li><li>RESUME</li><li>CONTACT US</li></ul></nav>
<div class="abs search">Search...
  <svg width="13" height="13" viewBox="0 0 13 13"><circle cx="5" cy="5" r="4" fill="none" stroke="#666" stroke-width="1.6"/><path d="M8 8l4 4" stroke="#666" stroke-width="2"/></svg>
</div>

<div class="abs stage"></div>
<div class="abs shadow"></div>
<section class="abs banner">
  <div class="abs banner-photo" role="img" aria-label="Photo of Mervin Tolle receiving an award at a labour relations seminar"></div>
  <div class="abs caption">Mervin Tolle (BA, MA, PhD) is a Professor in the Department of Management at Hong Kong</div>
  <div class="abs tabs">
    <div class="tab"><span>#2 Mervin Tolle Pics</span></div>
    <div class="tab"><span>#3 Mervin Tolle Pics</span></div>
    <div class="tab"><span>#4 Mervin Tolle Pics</span></div>
    <div class="tab"><span>#5 Mervin Tolle Pics</span></div>
  </div>
</section>

<h1 class="page-title">Harbourview University and Director of the Centre.</h1>
<div class="abs intro-photo"><div role="img" aria-label="Photo of faculty members playing football at a campus event"></div></div>
<p class="abs intro">Prof. Tolle previously served as the Head of the Department of <b><i>Management at HVU for nine years and on more than 30 university</i></b> committees, including the Task Force on Medical and Dental Benefits Review (Chairman), Non-teaching Staff Salary Review Conversion Panel (Chairman), and the Steering Committee on Review of the Pay and Reward Structure.&nbsp; At present, he serves on the University Senate as well as the University Council.&nbsp; Prof. Tolle is also a subject matter expert in HRM for the Hong Kong .</p>
<p class="abs intro2">Prof. Tolle's research interests include labor relations, personnel psychology, equal opportunities, and professional ethics. He has published over 100 academic articles, book chapters, and conference papers in scientific journals such as Journal of Workplace Studies.</p>
<div class="abs readmore">Read More</div>

<article class="abs card" style="left:111px;top:821px">
  <div class="frame"><div class="pic" role="img" aria-label="Photo from an employee assistance programme seminar" style="background:linear-gradient(120deg,#dfe6ee,#8fa0b3)"><b>Career History</b></div></div>
  <p><b>Contrary to popular</b> belief, is not simply Lorem Ipsum is not simply random text. It has roots in a piece of classical.</p>
  <span class="more">More [+].</span>
</article>
<article class="abs card" style="left:347px;top:821px">
  <div class="frame"><div class="pic" role="img" aria-label="Photo of a speaker at an annual dinner" style="background:linear-gradient(120deg,#c9a35a,#3c3424 60%,#6d5a3a)"><b>Educational Achieve</b></div></div>
  <p><b>Contrary to popular</b> belief, is not simply Lorem Ipsum is not simply random text. It has roots in a piece of classical.</p>
  <span class="more">More [+].</span>
</article>
<article class="abs card" style="left:579px;top:821px">
  <div class="frame"><div class="pic" role="img" aria-label="Photo of an award presentation at a talent management summit" style="background:linear-gradient(120deg,#6a4f3a,#e7a334 55%,#f3cf6a)"><b>Memberships</b></div></div>
  <p><b>Contrary to popular</b> belief, is not simply Lorem Ipsum is not simply random text. It has roots in a piece of classical.</p>
  <span class="more">More [+].</span>
</article>

<aside class="abs side" style="top:529px;height:256px">
  <h2>Lastest News</h2>
  <div class="news"><div class="thumb" role="img" aria-label="News thumbnail"></div><p>Lorem Ipsum is simply text of the also a subject matter <span>printing</span></p><i>May 15 , 2012</i></div>
  <div class="news"><div class="thumb" role="img" aria-label="News thumbnail"></div><p>Lorem Ipsum is simply text of the also a subject matter <span>printing</span></p><i>May 15 , 2012</i></div>
  <div class="news"><div class="thumb" role="img" aria-label="News thumbnail"></div><p>Lorem Ipsum is simply text of the also a subject matter <span>printing</span></p><i>May 15 , 2012</i></div>
</aside>
<aside class="abs side" style="top:804px;height:256px;left:817px">
  <h2>Tesimonials</h2>
  <p class="quote">Contrary to popular belief, Lorem Ipsum is not simply random text. It has roots in a piece of classical Latin literature from 45 BC, making it over 2000 years old. Edwin Marlowe from 45 BC, making it over 2000 years old. Edwin Marlowe, a Latin professor at Ashgrove College</p>
</aside>

<footer class="abs footer"></footer>
<div class="abs brand footer-brand" style="left:132px;top:1120px"><span>Harbourview<br>School</span><span class="dot"></span></div>
<div class="abs foot-nav">Home &nbsp; | &nbsp; About &nbsp; | &nbsp; Bio &nbsp; | &nbsp; Resume &nbsp; | &nbsp; Contact us</div>
<div class="abs copy">Copyright © 2012 - harbourviewschool - All rights reserved. Terms and Privacy Policy</div>
<div class="abs addr"><b>Address Line 1 with City</b><br><b>Address Line 2 with Country</b><br>Tel. : 123 . 456 . 7890<br><span style="line-height:24px">Email : <span style="color:#ddd">info@harbourviewschool.com</span></span></div>
</body>
</html>
```